bail bonds business

Need a web design for a Bail Bond company. At Larkmoor Bails, we specialize in getting arrested defendants out of jail. Also, I have all the necessary information already uploaded in the files.

Target Market(s)

Arrested defendants and their families who will post bails on their behalf.

Industry/Entity Type

Business

Coding

Coded - Design and coding required

Number of Pages Required

1 page

```html
<!DOCTYPE html>
<html lang="en">
<head>
<meta charset="utf-8">
<title>Larkmoor Bails</title>
<link rel="stylesheet" href="https://fonts.googleapis.com/css2?family=Playfair+Display:ital,wght@0,400;0,700;1,400&family=Open+Sans:wght@400;600;700&display=swap">
<style>
:root{
  --red:#c0182a;
  --red-deep:#8e0f1d;
  --ink:#1b1b1b;
  --dark:#262626;
  --grey:#7a7a7a;
  --light:#f2f2f2;
  --white:#ffffff;
}
*{box-sizing:border-box;margin:0;padding:0}
html,body{width:1200px;height:2224px;overflow:hidden}
body{font-family:"Open Sans",Arial,sans-serif;color:var(--ink);background:var(--white);position:relative}
.serif{font-family:"Playfair Display",Georgia,serif}

.topbar{position:absolute;left:0;top:0;width:1200px;height:40px;background:var(--light);display:flex;align-items:center;justify-content:space-between;padding:0 120px;font-size:12px;color:var(--grey)}
.topbar .phones{display:flex;gap:28px}
.topbar .phones span{display:flex;align-items:center;gap:6px}
.topbar .social{display:flex;gap:6px}
.topbar .social i{display:block;width:20px;height:20px;background:var(--red)}

.nav{position:absolute;left:0;top:40px;width:1200px;height:104px;background:var(--white);display:flex;align-items:center;justify-content:space-between;padding:0 120px;border-bottom:1px solid #e4e4e4}
.brand{display:flex;align-items:center;gap:12px;font-weight:700;font-size:24px;color:var(--red-deep)}
.brand i{display:block;width:34px;height:34px;background:var(--red)}
.nav ul{list-style:none;display:flex;gap:34px;font-size:12px;font-weight:600;letter-spacing:1px;color:#555}
.nav li.active{color:var(--red)}

.hero{position:absolute;left:0;top:144px;width:1200px;height:416px;background:linear-gradient(90deg,#e9e9e9,#fafafa)}
.hero .photo{position:absolute;left:0;top:0;width:640px;height:416px;background:linear-gradient(180deg,#d9d9d9,#bdbdbd)}
.hero h1{position:absolute;left:650px;top:120px;font-family:"Playfair Display",Georgia,serif;font-weight:400;font-size:58px;line-height:1.15;color:var(--red)}
.hero h1 em{font-style:italic}
.hero .perks{position:absolute;left:160px;top:356px;display:flex;gap:8px}
.perk{width:210px;height:60px;background:rgba(20,20,20,.82);display:flex;align-items:center;gap:12px;padding:0 14px;color:var(--white);font-size:11px;line-height:1.3}
.perk i{flex:none;display:block;width:34px;height:34px;background:var(--red)}

.about{position:absolute;left:0;top:560px;width:1200px;height:500px;background:var(--white)}
.about .card{position:absolute;left:192px;top:160px;width:370px;height:260px;background:var(--ink);color:var(--white);padding:56px 44px;box-shadow:-12px 12px 0 var(--red)}
.about .card h2{font-family:"Playfair Display",Georgia,serif;font-size:56px;font-weight:400;letter-spacing:2px;line-height:1}
.about .card p{margin-top:22px;font-size:13px;line-height:1.6;color:#d6d6d6;width:250px}
.about .portrait{position:absolute;left:680px;top:40px;width:360px;height:420px;background:linear-gradient(180deg,#e6e6e6,#9a9a9a)}
.about .caption{position:absolute;left:600px;top:420px;width:440px;height:44px;background:var(--red);color:var(--white);font-size:15px;font-weight:600;display:flex;align-items:center;padding-left:30px}

.offer{position:absolute;left:0;top:1060px;width:1200px;height:480px;background:linear-gradient(135deg,#2d2d2d,#161616);color:var(--white)}
.offer h2{position:absolute;left:100px;top:120px;font-family:"Playfair Display",Georgia,serif;font-weight:400;font-size:64px;line-height:1.05;letter-spacing:2px}
.offer h2 .accent{color:var(--red)}
.offer .lead{position:absolute;left:100px;top:272px;font-size:17px;color:#e0e0e0}
.offer .grid{position:absolute;left:460px;top:90px;width:620px;display:grid;grid-template-columns:repeat(3,1fr);row-gap:60px}
.service{display:flex;flex-direction:column;align-items:center;gap:14px;font-size:14px}
.service .icon{width:72px;height:72px;border-radius:50%;background:var(--white);display:flex;align-items:center;justify-content:center}
.service .icon.hot{background:var(--red)}

.area{position:absolute;left:0;top:1540px;width:1200px;height:360px;background:var(--white)}
.area .card{position:absolute;left:80px;top:40px;width:340px;height:270px;background:var(--red);color:var(--white);padding:40px 36px;box-shadow:12px 12px 0 var(--ink)}
.area .card h2{font-family:"Playfair Display",Georgia,serif;font-weight:400;font-size:50px;line-height:1.02;letter-spacing:1px}
.area .card p{margin-top:18px;font-size:12px;line-height:1.55}
.area .copy{position:absolute;left:470px;top:50px;width:660px;font-size:13px;line-height:1.8;color:var(--grey)}

.contact{position:absolute;left:0;top:1900px;width:1200px;height:324px;background:linear-gradient(180deg,#b3172a,#7e0d19);color:var(--white);text-align:center;padding-top:48px}
.contact p{font-family:"Playfair Display",Georgia,serif;font-size:46px;line-height:1.18}
</style>
</head>
<body>

<header>
  <div class="topbar">
    <div class="phones">
      <span><svg width="12" height="12" viewBox="0 0 24 24"><path fill="#c0182a" d="M6.6 10.8a15 15 0 006.6 6.6l2.2-2.2c.3-.3.7-.4 1-.2 1.1.4 2.3.6 3.6.6.6 0 1 .4 1 1V20c0 .6-.4 1-1 1C10.6 21 3 13.4 3 4c0-.6.4-1 1-1h3.5c.6 0 1 .4 1 1 0 1.3.2 2.5.6 3.6.1.3 0 .7-.2 1z"/></svg>716-555-0142</span>
      <span><svg width="12" height="12" viewBox="0 0 24 24"><path fill="#c0182a" d="M6.6 10.8a15 15 0 006.6 6.6l2.2-2.2c.3-.3.7-.4 1-.2 1.1.4 2.3.6 3.6.6.6 0 1 .4 1 1V20c0 .6-.4 1-1 1C10.6 21 3 13.4 3 4c0-.6.4-1 1-1h3.5c.6 0 1 .4 1 1 0 1.3.2 2.5.6 3.6.1.3 0 .7-.2 1z"/></svg>716-555-0187</span>
    </div>
    <div class="social"><i></i><i></i><i></i></div>
  </div>
  <nav class="nav">
    <div class="brand"><i></i>Larkmoor Bails</div>
    <ul>
      <li class="active">HOME</li>
      <li>ABOUT US</li>
      <li>WHAT WE OFFER</li>
      <li>OUR SERVICE AREA</li>
    </ul>
  </nav>
</header>

<section class="hero">
  <div class="photo" role="img" aria-label="Photo of three smiling professionals in business attire"></div>
  <h1>We bring <em>families</em><br>together.</h1>
  <div class="perks">
    <div class="perk"><i></i>Your freedom starts with Larkmoor</div>
    <div class="perk"><i></i>Larkmoor gets you out of jail fast</div>
    <div class="perk"><i></i>We guarantee your bail</div>
  </div>
</section>

<section class="about">
  <div class="card">
    <h2>ABOUT US</h2>
    <p>At Larkmoor Bails, getting your loved one out of jail very quickly is our priority.</p>
  </div>
  <div class="portrait" role="img" aria-label="Portrait of the company founder in a dark suit"></div>
  <div class="caption">Daniel Ferrow, LLB MBA</div>
</section>

<section class="offer">
  <h2>WHAT <span class="accent">WE</span><br>OFFER</h2>
  <p class="lead">At Larkmoor Bails, we deal with</p>
  <div class="grid">
    <div class="service"><div class="icon"><svg width="36" height="36" viewBox="0 0 36 36"><circle cx="11" cy="22" r="7" fill="none" stroke="#c0182a" stroke-width="3"/><circle cx="25" cy="22" r="7" fill="none" stroke="#c0182a" stroke-width="3"/><path d="M16 14h4" stroke="#c0182a" stroke-width="3"/></svg></div>Felony Bails</div>
    <div class="service"><div class="icon"><svg width="36" height="36" viewBox="0 0 36 36"><rect x="8" y="14" width="20" height="8" rx="4" fill="#c0182a"/><rect x="18" y="14" width="10" height="8" rx="4" fill="#262626"/></svg></div>Drug Charges bails</div>
    <div class="service"><div class="icon hot"><svg width="36" height="36" viewBox="0 0 36 36"><circle cx="18" cy="15" r="8" fill="none" stroke="#fff" stroke-width="3"/><path d="M18 23v9M13 28h10" stroke="#fff" stroke-width="3"/></svg></div>Sex Crime bails</div>
    <div class="service"><div class="icon"><svg width="36" height="36" viewBox="0 0 36 36"><path d="M6 22l4-9h16l4 9v6H6z" fill="#c0182a"/><circle cx="11" cy="28" r="3" fill="#262626"/><circle cx="25" cy="28" r="3" fill="#262626"/></svg></div>DUI bails</div>
    <div class="service"><div class="icon hot"><svg width="36" height="36" viewBox="0 0 36 36"><path d="M10 8h16v20H10z" fill="none" stroke="#fff" stroke-width="3"/><path d="M14 15h8M14 21h8" stroke="#fff" stroke-width="3"/></svg></div>Theft bails</div>
    <div class="service"><div class="icon"><svg width="36" height="36" viewBox="0 0 36 36"><path d="M9 6h14l5 5v19H9z" fill="none" stroke="#c0182a" stroke-width="3"/><path d="M13 18l4 4 7-8" fill="none" stroke="#c0182a" stroke-width="3"/></svg></div>24/7 Notary Public service</div>
  </div>
</section>

<section class="area">
  <div class="card">
    <h2>OUR<br>SERVICES<br>AREA</h2>
    <p>Serving all of western New York. At Larkmoor, we work with care at a professional and efficient level.</p>
  </div>
  <p class="copy">Larkmoor Bails serves defendants and families across Erie, Niagara, Genesee and Wyoming counties. When someone you love is arrested, every hour matters, so our agents answer the phone day and night and travel to any holding center in the region. We explain the bail process in plain words, help you gather the paperwork and post the bond as fast as the court allows. Our fees follow state rules, and payment plans are available for families who need them. From the first call until the final court date, we stay beside you and keep you informed at every step.</p>
</section>

<footer class="contact" role="img" aria-label="Red-toned city photo behind contact details">
  <p>Phone: 716-555-0142</p>
  <p>Fax: 716-555-0187</p>
  <p>Address: 412 Alder Row,</p>
  <p>Suite 2B Marlow, NY 14200</p>
</footer>

</body>
</html>
```